Velmora Trade Hall (front page)

We need a design of a front page for our Velmora Trade Hall website (vth.co.uk). Our company is based in the United Kingdom and offers investors from all over the world an opportunity to invest into bitcoin and litecoin.

We have been developing this cutting edge technology for past 2 years based on our in depth knowledge on conventional stock and currency trading technology and methodology. We have run many test against penetration, security and stability and now are ready to deploy.

Recent news about vulnerability of such platforms leave a great deal of unease from retail investors about investing into cryptocurrency. We are set to challenge this attitude. Our background is payments in particular regulated environment in the UK. We are keen to apply our wealth of experience to provide secure and reliable trading platform and advance cryptocurrency as means of legal tender.

The front page should be based on the feel and look of our current technology vth.co.uk. Some of you have already been involved in logo design for our company, please see the attached mockups. The page should have this minimalist design, very clean and light.

Seek inspiration form www.korvelin.net, www.trusmarq.com, vip.plomwerth.com and other bitcoin exchanges.

We look forward to receiving your ideas.

You can also refer to our social pages:
https://www.facebook.com/vth.co.uk
https://twitter.com/vth_uk

We would like you to focus your efforts at designing the page in such a way so that it is very easy for visitor be open an account with the exchange. We must focus at informing the visitor about the bitcoin, how to my buy, how to sell, look at the general overview of the maker and CONVERTING him/her sing up. This is the most important!!

Regards,
Oren

Reason: Dear all, We are very keen on getting this design done right the first time. The key success is conversion of visitors to subscribers and then to traders. It is absolutely essential make the registration process as streamlined as possible! When we are calling them to act by "Change the world one bitcoin at a time" we should give them a opportunity to provide us with relevant account creation details: email, password, confirm password. Please visit quenzo.co.uk for ideas. Secondly, tell them what is a bitcoin, why a bitcoin is a good investment and how to invest. Finally, it is important to inform visitors of "who we are", what sets us apart from other exchanges, tell them about our experience. In our view graphs and live order books are important but they might turn some visitors away especially the ones that are not accustomed to online trading. Think of what would you like to see on the page if you wanted YOURSELF to invest. What would make you to create an account and use it? Think what will work, we are here to revolutionise how people do business.... any wild ideas put them to us. OUR BUDGET JUST GONE UP!!!

Target Market(s)

A combination of professional and consumer bitcoin investors.

Requirements
Must have
• News section

```html
<!DOCTYPE html>
<html lang="en">
<head>
<meta charset="utf-8">
<title>Velmora Trade Hall</title>
<link href="https://fonts.googleapis.com/css2?family=Open+Sans:wght@400;600;700&family=Oswald:wght@400;500&family=Kaushan+Script&display=swap" rel="stylesheet">
<style>
:root{
  --ink:#3c3c3c;
  --muted:#8a8a8a;
  --blue:#3fa9dc;
  --blue-deep:#2b8fc4;
  --hero:#45b0e0;
  --orange:#f7941d;
  --orange-soft:#fde9c8;
  --green:#6cbf3a;
  --dark:#1f1f1f;
  --dark-box:#3d3d3d;
  --grey-bg:#f2f2f2;
  --line:#e1e1e1;
  --cyan-soft:#e4f7fa;
  --slate:#8fb3c7;
  --white:#ffffff;
}
*{box-sizing:border-box;margin:0;padding:0}
html,body{width:1200px;height:3666px;overflow:hidden}
body{font-family:"Open Sans",Arial,sans-serif;color:var(--ink);background:var(--white);font-size:14px}
section,header,footer{position:relative;width:1200px}
.abs{position:absolute}

/* top bar */
.ticker-bar{height:49px;background:var(--dark);color:#9a9a9a}
.ticker{position:absolute;top:7px;font-size:12px;line-height:15px}
.ticker b{display:block;color:var(--blue);font-size:15px;font-weight:600}
.lang{position:absolute;left:784px;top:12px;width:82px;height:26px;background:#3a3a3a;color:#ddd;font-size:12px;padding:5px 10px;border-radius:2px}
.lang:after{content:"";position:absolute;right:9px;top:11px;border:4px solid transparent;border-top-color:#ddd}
.top-btn{position:absolute;top:11px;height:28px;padding:0 12px;line-height:28px;color:#fff;font-size:12px;font-weight:700;border-radius:2px}
.top-btn.signup{left:876px;background:var(--orange)}
.top-btn.login{left:951px;background:var(--blue)}

/* header */
.site-header{height:129px;background:#fff;border-bottom:1px solid var(--line)}
.brand{position:absolute;left:175px;top:50px;display:flex;align-items:center;gap:12px}
.brand-name{font-size:17px;font-weight:600;letter-spacing:4px;color:#333;text-transform:uppercase}
.brand-dot{width:24px;height:24px;border-radius:50%;background:var(--blue)}
.nav{position:absolute;left:557px;top:48px;display:flex;gap:6px}
.nav a{display:block;padding:0 12px;height:34px;line-height:34px;font-size:14px;color:#444;text-decoration:none;border-radius:2px}
.nav a.active{background:var(--blue);color:#fff}

/* hero */
.hero{height:322px;background:var(--hero);z-index:2}
.hero-map{position:absolute;left:200px;top:10px;width:800px;height:290px;border-radius:40%;background:radial-gradient(ellipse at center,rgba(255,255,255,.16),rgba(255,255,255,0) 70%)}
.hero-icons{position:absolute;left:478px;top:42px;display:flex;gap:27px}
.hero-icon{width:62px;height:62px;border-radius:50%;background:#fff;display:flex;align-items:center;justify-content:center}
.hero-dots{position:absolute;left:583px;top:126px;display:flex;gap:4px}
.hero-dots i{width:7px;height:7px;border-radius:50%;border:1.5px solid #fff}
.tagline{position:absolute;left:0;width:1200px;top:134px;text-align:center;font-family:"Kaushan Script",cursive;color:#fff;font-size:33px}
.hero-note{position:absolute;left:834px;top:222px;font-family:"Kaushan Script",cursive;color:#fff;font-size:19px;line-height:22px;transform:rotate(-6deg)}
.reg-box{position:absolute;left:469px;top:208px;width:264px;height:279px;background:var(--dark-box);border:6px solid #2e2e2e;padding:14px 14px;box-shadow:0 10px 14px rgba(0,0,0,.18)}
.reg-title{color:#fff;font-family:"Oswald",sans-serif;font-size:23px;letter-spacing:.5px;margin-bottom:12px}
.reg-title span{color:var(--orange)}
.reg-input{height:38px;background:#fff;border:1px solid #ccc;margin-bottom:10px;font-size:12px;padding:10px 8px;color:#555}
.reg-submit{height:42px;margin-top:6px;background:var(--orange);color:#fff;text-align:center;line-height:42px;font-family:"Oswald",sans-serif;font-size:17px;border-bottom:3px solid #d97a0d}

/* features */
.features{height:593px}
.feature{position:absolute;top:209px;width:220px;text-align:center}
.feature-icon{width:86px;height:86px;border-radius:50%;margin:0 auto;display:flex;align-items:center;justify-content:center}
.feature h3{font-weight:400;font-size:19px;margin-top:42px;color:#444}
.feature p{margin-top:18px;font-size:13.5px;line-height:19px;color:#9a9a9a}

/* who we are */
.who{height:349px}
.section-head{position:absolute;display:flex;align-items:center;gap:12px;font-size:28px;font-weight:400}
.head-icon{width:56px;height:56px;border-radius:50%;display:flex;align-items:center;justify-content:center}
.who-head{left:180px;top:18px;color:var(--blue)}
.who-head em{font-style:normal;color:var(--green)}
.who-lead{position:absolute;left:186px;top:92px;width:540px;font-size:13px;line-height:20px;font-weight:700;color:#444}
.who-list{position:absolute;left:186px;top:152px;list-style:none}
.who-list li{font-size:13px;font-weight:700;line-height:31px;color:#444;display:flex;align-items:center;gap:10px}
.tick{width:15px;height:15px;border-radius:50%;background:var(--green);display:inline-flex;align-items:center;justify-content:center}
.bolt{position:absolute;left:836px;top:70px;width:60px;height:120px;background:linear-gradient(180deg,#bfe3f5,#5bb8e5);border-radius:30px}
.cta-caption{position:absolute;left:775px;top:205px;width:234px;text-align:center;font-family:"Oswald",sans-serif;font-size:20px;color:var(--orange)}
.cta-caption span{color:var(--green)}
.cta-join{position:absolute;left:782px;top:239px;width:220px;height:49px;line-height:49px;text-align:center;background:var(--blue);color:#fff;font-family:"Oswald",sans-serif;font-size:19px;border-bottom:3px solid var(--blue-deep)}

/* market */
.market{height:1528px;background:var(--grey-bg);border-top:1px solid var(--line)}
.overview-head{left:180px;top:40px;color:var(--orange)}
.chart-box{position:absolute;left:196px;top:115px;width:806px;height:301px;background:#fff;border:1px solid var(--line)}
.trades{position:absolute;left:196px;top:476px;width:806px;border-collapse:collapse;background:#fff;font-size:11px;color:#555}
.trades th{background:#e9e9e9;text-align:left;font-weight:600;height:41px;padding-left:10px;color:#444}
.trades td{height:38px;padding-left:10px;border-top:1px solid #ececec}
.trades tr.sell td{background:var(--orange-soft)}
.divider{position:absolute;left:196px;top:904px;width:806px;height:2px;background:#e3e3e3}
.trade-panel{position:absolute;left:196px;top:946px;width:391px;height:405px}
.trade-tabs{display:flex;height:42px}
.trade-tab{width:112px;text-align:center;font-size:12px;line-height:15px;padding-top:6px;color:#888;background:#e6e6e6}
.trade-tab b{display:block;font-weight:600;color:var(--blue)}
.trade-tab.active{background:#fff}
.trade-tab.active b{color:var(--orange)}
.trade-body{background:#fff;height:363px;padding:18px 20px;border:1px solid var(--line);border-top:none}
.trade-row{display:flex;align-items:center;height:52px;font-size:12px;color:#777}
.trade-row label{width:118px}
.trade-field{flex:1;height:42px;background:#f0f0f0;border:1px solid #ddd;padding:12px 10px;color:#555;position:relative}
.trade-field.select:after{content:"";position:absolute;right:12px;top:18px;border:5px solid transparent;border-top-color:#888}
.trade-sum{border:1px solid #ddd;margin-top:8px}
.trade-sum div{display:flex;height:38px;align-items:center;font-size:12px;padding-left:10px;color:#555}
.trade-sum div+div{border-top:1px solid #ddd}
.trade-sum span{width:108px}
.trade-sum b{font-weight:700;color:#333}
.trade-actions{display:flex;justify-content:space-between;margin-top:20px}
.trade-btn{width:170px;height:48px;line-height:48px;text-align:center;color:#fff;font-size:12px;font-weight:700}
.trade-btn.sell{background:var(--orange)}
.trade-btn.cancel{background:var(--slate)}
.bidding-title{position:absolute;left:611px;top:956px;font-size:22px;color:var(--orange)}
.bidding{position:absolute;left:611px;top:998px;width:391px;border-collapse:collapse;background:#fff;font-size:11px;color:#555}
.bidding th{height:40px;text-align:left;padding-left:14px;color:var(--blue-deep);font-weight:700;border:1px solid #ddd}
.bidding td{height:35px;padding-left:14px;border:1px solid #e8e8e8;width:33.3%}
.bidding .ask-row td.price,.bidding .ask-row td.ask{background:var(--cyan-soft)}
.bidding .bid-row td.bid,.bidding .bid-row td.price{background:var(--orange-soft)}
.register-strip{position:absolute;left:196px;top:1405px;width:540px;font-size:12px;line-height:21px;color:#444}
.register-now{position:absolute;left:745px;top:1408px;width:257px;height:56px;line-height:56px;text-align:center;background:var(--orange);color:#fff;font-family:"Oswald",sans-serif;font-size:19px;border-bottom:3px solid #d97a0d}

/* news */
.news{height:610px;border-top:1px solid var(--line)}
.news-head{left:180px;top:37px;color:var(--blue)}
.news-card{position:absolute;top:114px;width:242px;height:406px;background:#fff;border:1px solid #e6e6e6;box-shadow:0 1px 3px rgba(0,0,0,.08);padding:14px 14px}
.news-card h4{font-size:13px;line-height:17px;color:var(--blue-deep);font-weight:700}
.news-date{font-size:12.5px;color:#333;margin:3px 0 8px}
.news-intro{display:flex;gap:10px}
.news-thumb{width:80px;height:88px;flex:none;background:linear-gradient(135deg,#cfe6f4,#6fa9d0)}
.news-intro p,.news-body{font-size:11px;line-height:15px;color:#666}
.news-body{margin-top:6px}
.know-more{position:absolute;left:56px;bottom:22px;width:128px;height:38px;line-height:38px;text-align:center;background:var(--slate);color:#fff;font-size:11px;font-weight:700}

/* footer */
.site-footer{height:86px;background:var(--dark);text-align:center}
.footer-nav{padding-top:24px;display:flex;justify-content:center;gap:30px}
.footer-nav a{color:var(--blue);font-size:12px;text-decoration:none}
.copyright{margin-top:12px;font-size:10.5px;color:#888}
</style>
</head>
<body>

<section class="ticker-bar">
  <div class="ticker" style="left:173px">Last price<b>13.72 EUR</b></div>
  <div class="ticker" style="left:316px">Low price<b>11.4 EUR</b></div>
  <div class="ticker" style="left:438px">High price<b>12.4 EUR</b></div>
  <div class="ticker" style="left:563px">Volum<b>197.4 LTC</b></div>
  <div class="lang">English</div>
  <div class="top-btn signup">SIGN UP</div>
  <div class="top-btn login">LOGIN</div>
</section>

<header class="site-header">
  <div class="brand"><span class="brand-name">Velmora Trade Hall</span><span class="brand-dot"></span></div>
  <nav class="nav">
    <a class="active" href="#">Home</a><a href="#">About</a><a href="#">API Trade</a><a href="#">Account</a><a href="#">Contacts</a><a href="#">Support</a>
  </nav>
</header>

<section class="hero">
  <div class="hero-map" role="img" aria-label="Faint world map in the background"></div>
  <div class="hero-icons">
    <div class="hero-icon"><svg width="34" height="34" viewBox="0 0 34 34"><circle cx="17" cy="17" r="14" fill="none" stroke="#45b0e0" stroke-width="3"/><path d="M17 9v9l6 4" fill="none" stroke="#45b0e0" stroke-width="3" stroke-linecap="round"/></svg></div>
    <div class="hero-icon"><svg width="34" height="34" viewBox="0 0 34 34"><circle cx="17" cy="17" r="14" fill="none" stroke="#45b0e0" stroke-width="3"/><ellipse cx="17" cy="17" rx="6" ry="14" fill="none" stroke="#45b0e0" stroke-width="2"/><path d="M3 17h28" stroke="#45b0e0" stroke-width="2"/></svg></div>
    <div class="hero-icon"><svg width="30" height="34" viewBox="0 0 30 34"><path d="M15 32C15 32 4 19 4 12a11 11 0 0 1 22 0c0 7-11 20-11 20z" fill="#45b0e0"/><circle cx="15" cy="12" r="4" fill="#fff"/></svg></div>
  </div>
  <div class="hero-dots"><i></i><i></i><i></i></div>
  <div class="tagline">Change the world one bitcoin at a time</div>
  <div class="hero-note">Register<br>for FREE</div>
  <svg class="abs" style="left:760px;top:215px" width="70" height="40" viewBox="0 0 70 40"><path d="M66 6C50 30 25 30 6 26" fill="none" stroke="#fff" stroke-width="2"/><path d="M14 19L5 26l10 5" fill="none" stroke="#fff" stroke-width="2"/></svg>
  <form class="reg-box">
    <div class="reg-title"><span>FREE</span> REGISTRATION</div>
    <div class="reg-input">Your Email Id</div>
    <div class="reg-input">Your Password</div>
    <div class="reg-input">Conform Password</div>
    <div class="reg-submit">JOIN US NOW</div>
  </form>
</section>

<section class="features">
  <div class="feature" style="left:193px">
    <div class="feature-icon" style="background:var(--orange)"><svg width="50" height="50" viewBox="0 0 50 50"><circle cx="25" cy="25" r="21" fill="none" stroke="#fff" stroke-width="3"/><circle cx="25" cy="25" r="12" fill="#fff"/></svg></div>
    <h3>What is Bitcon?</h3>
    <p>Lorem ipsum dolor sit amet, consec tetur adipiscing elit. Nam vulputate mauris id arcu pharetra, sed posuere quam cursus. Nullam eget massa vel mi posuere venenatis sed quis tortor. In hac habitasse platea dictumst.</p>
  </div>
  <div class="feature" style="left:494px">
    <div class="feature-icon" style="background:var(--green)"><svg width="50" height="50" viewBox="0 0 50 50"><path d="M8 12h6l5 20h18l4-14H17" fill="none" stroke="#fff" stroke-width="3" stroke-linejoin="round"/><circle cx="21" cy="38" r="3" fill="#fff"/><circle cx="35" cy="38" r="3" fill="#fff"/></svg></div>
    <h3>How to Buy Bitcoins?</h3>
    <p>Vestibulum ante ipsum primis in faucibus orci luctus et ultrices posuere cubilia Curae; Duis sagittis, risus ut viverra dignissim, lectus nunc iaculis arcu, et gravida est tortor ut erat. Nullam eget massa vel mi posuere venenatis sed quis tortor.</p>
  </div>
  <div class="feature" style="left:799px">
    <div class="feature-icon" style="background:var(--blue)"><svg width="50" height="50" viewBox="0 0 50 50"><rect x="8" y="10" width="34" height="24" rx="2" fill="none" stroke="#fff" stroke-width="3"/><path d="M18 40h14M25 34v6" stroke="#fff" stroke-width="3"/></svg></div>
    <h3>How to Sell Bitcons?</h3>
    <p>Vivamus faucibus ac leo ac dignissim. Nam vulputate mauris id arcu pharetra, sed posuere quam cursus. Nullam eget massa vel mi posuere venenatis sed quis tortor. In hac habitasse platea dictumst.</p>
  </div>
</section>

<section class="who">
  <div class="section-head who-head"><span class="head-icon" style="background:var(--blue)"><svg width="24" height="26" viewBox="0 0 24 26"><circle cx="12" cy="4" r="3" fill="#fff"/><rect x="9" y="10" width="6" height="14" rx="1.5" fill="#fff"/></svg></span>Who We Are and <em>Why should you choose us</em></div>
  <p class="who-lead">Lorem ipsum dolor sit amet, consectetur adipiscing elit. Sed quis nisi euismod, fermentum tellus a, lobortis quam.</p>
  <ul class="who-list">
    <li><span class="tick"><svg width="9" height="9" viewBox="0 0 9 9"><path d="M1 5l2 2 5-6" fill="none" stroke="#fff" stroke-width="1.8"/></svg></span>Vestibulum condimentum mi vitae diam tristique</li>
    <li><span class="tick"><svg width="9" height="9" viewBox="0 0 9 9"><path d="M1 5l2 2 5-6" fill="none" stroke="#fff" stroke-width="1.8"/></svg></span>Dignissim diam mattis urabitur vel diam in massa</li>
    <li><span class="tick"><svg width="9" height="9" viewBox="0 0 9 9"><path d="M1 5l2 2 5-6" fill="none" stroke="#fff" stroke-width="1.8"/></svg></span>Vivamus faucibus ac leo ac dignissim.</li>
    <li><span class="tick"><svg width="9" height="9" viewBox="0 0 9 9"><path d="M1 5l2 2 5-6" fill="none" stroke="#fff" stroke-width="1.8"/></svg></span>Maecenas orci est, euismod facilisis feugiat sit amet</li>
    <li><span class="tick"><svg width="9" height="9" viewBox="0 0 9 9"><path d="M1 5l2 2 5-6" fill="none" stroke="#fff" stroke-width="1.8"/></svg></span>Donec eleifend accumsan nisl, nec laoreet leo iaculis sit amet.</li>
  </ul>
  <div class="bolt" role="img" aria-label="Light blue lightning bolt illustration"></div>
  <div class="cta-caption">REGISTER <span>FOR FREE ACCOUNT</span></div>
  <div class="cta-join">JOIN US NOW</div>
</section>

<section class="market">
  <div class="section-head overview-head"><span class="head-icon" style="background:var(--orange)"><svg width="26" height="22" viewBox="0 0 26 22"><g fill="#fff"><circle cx="3" cy="3" r="2.5"/><circle cx="3" cy="11" r="2.5"/><circle cx="3" cy="19" r="2.5"/><rect x="8" y="1" width="18" height="4"/><rect x="8" y="9" width="18" height="4"/><rect x="8" y="17" width="18" height="4"/></g></svg></span>Overview</div>

  <div class="chart-box">
    <svg width="806" height="301" viewBox="0 0 806 301" font-family="Open Sans, sans-serif" font-size="9" fill="#888">
      <g><rect x="6" y="6" width="22" height="14" fill="#eee"/><text x="10" y="16">M1</text><rect x="30" y="6" width="22" height="14" fill="#eee"/><text x="34" y="16">M5</text><rect x="54" y="6" width="26" height="14" fill="#eee"/><text x="57" y="16">M15</text><rect x="82" y="6" width="26" height="14" fill="#eee"/><text x="85" y="16">M30</text><rect x="110" y="6" width="22" height="14" fill="#eee"/><text x="115" y="16">H1</text><rect x="134" y="6" width="22" height="14" fill="#eee"/><text x="139" y="16">H4</text></g>
      <text x="403" y="20" text-anchor="middle" font-size="12" fill="#555">LTC/EUR</text>
      <line x1="60" y1="40" x2="806" y2="40" stroke="#eee"/><line x1="60" y1="120" x2="806" y2="120" stroke="#eee"/><line x1="60" y1="160" x2="806" y2="160" stroke="#eee"/>
      <text x="30" y="50">12.269</text><text x="40" y="124">11.8</text><text x="40" y="164">11.5</text>
      <path d="M60 45H510L560 80 610 130 660 190 700 195 720 192H806V250H60Z" fill="#dcedf8"/>
      <path d="M60 45H510L560 80 610 130 660 190 700 195 720 192H806" fill="none" stroke="#8fc5e6" stroke-width="2"/>
      <line x1="470" y1="40" x2="470" y2="250" stroke="#c9c9c9"/>
      <circle cx="470" cy="45" r="3.5" fill="#fff" stroke="#5aa9dc" stroke-width="1.5"/>
      <rect x="478" y="37" width="74" height="34" fill="#fff" stroke="#ccc"/>
      <text x="484" y="50" font-size="8">● 4:18:00 PM</text><text x="484" y="64" font-size="9" fill="#555">12.05613</text>
      <text x="70" y="220">15:45</text><text x="190" y="220">15:05</text><text x="350" y="220">16:05</text><text x="560" y="220">16:15</text><text x="690" y="220">16:25</text>
      <line x1="0" y1="262" x2="806" y2="262" stroke="#e2e2e2"/>
      <line x1="270" y1="262" x2="270" y2="301" stroke="#e2e2e2"/><line x1="537" y1="262" x2="537" y2="301" stroke="#e2e2e2"/>
      <text x="135" y="286" text-anchor="middle" font-size="9" fill="#555">QUOTES</text><text x="403" y="286" text-anchor="middle">CANDLES</text><text x="671" y="286" text-anchor="middle">VOLUME</text>
    </svg>
  </div>

  <table class="trades">
    <thead><tr><th>Market</th><th>Time</th><th>Type</th><th>Volume (LTC)</th><th>Price</th><th>Total (EUR)</th></tr></thead>
    <tbody>
      <tr><td>LTC/EUR</td><td>3/18/2014 10:54:50 PM</td><td>Buy</td><td>6.87191</td><td>13.72</td><td>94.2826</td></tr>
      <tr><td>LTC/EUR</td><td>3/18/2014 10:50:04 PM</td><td>Buy</td><td>0.11408</td><td>13.624</td><td>1.5542</td></tr>
      <tr><td>LTC/EUR</td><td>3/18/2014 10:43:48 PM</td><td>Buy</td><td>7.54633</td><td>13.549</td><td>102.2452</td></tr>
      <tr><td>LTC/EUR</td><td>3/18/2014 10:36:13 PM</td><td>Buy</td><td>5.34759</td><td>13.598</td><td>72.7165</td></tr>
      <tr class="sell"><td>LTC/EUR</td><td>3/18/2014 10:23:35 PM</td><td>Sell</td><td>1.82485</td><td>13.507</td><td>24.6482</td></tr>
      <tr><td>LTC/EUR</td><td>3/18/2014 10:54:50 PM</td><td>Buy</td><td>6.87191</td><td>13.72</td><td>94.2826</td></tr>
      <tr><td>LTC/EUR</td><td>3/18/2014 10:50:04 PM</td><td>Buy</td><td>0.11408</td><td>13.624</td><td>1.5542</td></tr>
      <tr><td>LTC/EUR</td><td>3/18/2014 10:43:48 PM</td><td>Buy</td><td>7.54633</td><td>13.549</td><td>102.2452</td></tr>
      <tr><td>LTC/EUR</td><td>3/18/2014 10:36:13 PM</td><td>Buy</td><td>5.34759</td><td>13.598</td><td>72.7165</td></tr>
      <tr class="sell"><td>LTC/EUR</td><td>3/18/2014 10:23:35 PM</td><td>Sell</td><td>1.82485</td><td>13.507</td><td>24.6482</td></tr>
    </tbody>
  </table>

  <div class="divider"></div>

  <div class="trade-panel">
    <div class="trade-tabs">
      <div class="trade-tab active"><b>Buy LTC</b>11.50200 EUR</div>
      <div class="trade-tab"><b>Sell LTC</b>11.38100 EUR</div>
    </div>
    <div class="trade-body">
      <div class="trade-row"><label>Type</label><div class="trade-field select">Limit</div></div>
      <div class="trade-row"><label>Volume LTC</label><div class="trade-field"></div></div>
      <div class="trade-row"><label>Price per LTC</label><div class="trade-field"></div></div>
      <div class="trade-sum">
        <div><span>Total :</span><b>EUR 0.00</b></div>
        <div><span>Fee :</span><b>EUR 0.00</b></div>
      </div>
      <div class="trade-actions"><div class="trade-btn sell">SELL LTC</div><div class="trade-btn cancel">CANCEL</div></div>
    </div>
  </div>

  <div class="bidding-title">Bidding</div>
  <table class="bidding">
    <thead><tr><th>BID</th><th>PRICE</th><th>ASK</th></tr></thead>
    <tbody>
      <tr class="ask-row"><td class="bid"></td><td class="price">11.87000</td><td class="ask">5.79603</td></tr>
      <tr class="ask-row"><td class="bid"></td><td class="price">11.86000</td><td class="ask">0.25862</td></tr>
      <tr class="ask-row"><td class="bid"></td><td class="price">11.81100</td><td class="ask">3.70862</td></tr>
      <tr class="ask-row"><td class="bid"></td><td class="price">11.80800</td><td class="ask">56.10440</td></tr>
      <tr class="ask-row"><td class="bid"></td><td class="price">11.80600</td><td class="ask">0.24006</td></tr>
      <tr class="bid-row"><td class="bid">1.35484</td><td class="price">11.61100</td><td class="ask"></td></tr>
      <tr class="bid-row"><td class="bid">0.23305</td><td class="price">11.57100</td><td class="ask"></td></tr>
      <tr class="bid-row"><td class="bid">0.78467</td><td class="price">11.55000</td><td class="ask"></td></tr>
      <tr class="bid-row"><td class="bid">1.35484</td><td class="price">11.61100</td><td class="ask"></td></tr>
    </tbody>
  </table>

  <p class="register-strip">Vestibulum ante ipsum primis in faucibus orci luctus et ultrices posuere cubilia Curae; Duis sagittis, risus ut viverra dignissim, lectus nunc iaculis arcu, et gravida est tortor ut erat.</p>
  <div class="register-now">REGISTER NOW</div>
</section>

<section class="news">
  <div class="section-head news-head"><span class="head-icon" style="background:var(--green)"><svg width="28" height="24" viewBox="0 0 28 24"><path d="M3 9h5l12-7v20L8 15H3z" fill="#fff"/><path d="M7 15l2 7h4l-2-7" fill="#fff"/></svg></span>News</div>

  <article class="news-card" style="left:191px">
    <h4>Fusce nisi tellus, fermentum a luctus eget</h4>
    <div class="news-date">27th February 2014</div>
    <div class="news-intro"><div class="news-thumb" role="img" aria-label="Blue chart graphic for the news item"></div><p>Lorem ipsum dolor sit amet, consectetur adipiscing elit. Sed quis nisi euismod, fermentum</p></div>
    <p class="news-body">estibulum condimentum mi vitae diam tristique, egestas dignissim diam mattis. Curabitur vel diam in massa porttitor dictum id in lorem. Vivamus faucibus ac leo ac dignissim. Maecenas orci est, euismod facilisis feugiat sit amet, semper ut tortor</p>
    <div class="know-more">KNOW MORE &#9656;</div>
  </article>
  <article class="news-card" style="left:477px">
    <h4>Aenean gravida nisl ut ligula facilisis, sed sollicitudin</h4>
    <div class="news-date">7th March 2014</div>
    <div class="news-intro"><div class="news-thumb" role="img" aria-label="Photo of a business handshake"></div><p>Sed quis nisi euismod, fermentum tellus a, lobortis quam estibulum vivamus faucibus leo ac</p></div>
    <p class="news-body">estibulum condimentum mi vitae diam tristique, egestas dignissim diam mattis. Curabitur vel diam in massa porttitor dictum id in lorem. Vivamus faucibus ac leo ac dignissim. Maecenas orci est, euismod facilisis feugiat sit amet, semper ut tortor</p>
    <div class="know-more">KNOW MORE &#9656;</div>
  </article>
  <article class="news-card" style="left:760px">
    <h4>Praesent cursus lacus ac eros feugiat, vitae eleifend</h4>
    <div class="news-date">18th March 2014</div>
    <div class="news-intro"><div class="news-thumb" role="img" aria-label="Illustration of a connected team"></div><p>Lorem ipsum dolor sit amet, consectetur adipiscing elit. Sed quis nisi euismod, fermentum</p></div>
    <p class="news-body">estibulum condimentum mi vitae diam tristique, egestas dignissim diam mattis. Curabitur vel diam in massa porttitor dictum id in lorem. Vivamus faucibus ac leo ac dignissim. Maecenas orci est, euismod facilisis feugiat sit amet, semper ut tortor</p>
    <div class="know-more">KNOW MORE &#9656;</div>
  </article>
</section>

<footer class="site-footer">
  <nav class="footer-nav"><a href="#">Home</a><a href="#">About</a><a href="#">API Trade</a><a href="#">Account</a><a href="#">Contacts</a><a href="#">Support</a></nav>
  <p class="copyright">© 2014 Velmora Trade Hall Limited. All rights reserved</p>
</footer>

</body>
</html>
```